International Freight Forwarder need a business card

We need a logo design for a freight forwarding company . We are active in Sea Transportation, Truck transportation, and Air Transportation, The design should be have normal dimensions of a card and should not have cuts and holes in its design (printed design is required - lamination accepted)

The said company is agent and sales representative of 2 other Shipping companies (whose logos, name, and website should also be mentioned on the card)

Industry/Entity Type

Logistics

Contact Information for Business Card

Address is "No.7, 2nd Sarv Baghestan-e-Nouri, Tehran, IR
Tel number is +98 21 66394512
Fax number is +98 21 66395830
E-Mail address is info@roshanbarsaz.com
Website is www.roshanbarsaz.com

Open Layer Logos attached as well

Colors
33a6d7
0292cd
0255a3
3276b5
85abd2
85cae6
cee9f5
d5e2ee
ffffff

Requirements
Must have
• Main logo of Roshan Barsaz
• Logo of TQM Shipping Line
• London, United Kingdom
• tqmline.com
• Logo of Calm Reef Shipping
• Dubai, United Arab Emirates
• crsuae.com
• We require OPEN layer file to be submitted to us upon project selection.
Should not have
• Weird Designs such as cuts to the shape or holes in design.

```html
<!DOCTYPE html>
<html lang="en">
<head>
<meta charset="utf-8">
<title>Roshan Barsaz – Business Card</title>
<link rel="stylesheet" href="https://fonts.googleapis.com/css2?family=Source+Sans+3:wght@400;600;700&display=swap">
<style>
  :root {
    --bg: #3d3632;
    --card: #0b0b0c;
    --accent: #33a6d7;
    --accent-strong: #0292cd;
    --navy: #0255a3;
    --mid-blue: #3276b5;
    --pale-blue: #85cae6;
    --silver: #c9ced4;
    --white: #ffffff;
  }
  * { margin: 0; padding: 0; box-sizing: border-box; }
  html, body { width: 1200px; height: 900px; overflow: hidden; }
  body {
    background: var(--bg);
    font-family: "Source Sans 3", sans-serif;
    color: var(--white);
    position: relative;
  }
  .card {
    position: absolute;
    top: 296px;
    width: 540px;
    height: 309px;
    background: var(--card);
    overflow: hidden;
    box-shadow: 0 10px 30px rgba(0,0,0,.45);
  }
  .card--front { left: 40px; }
  .card--back { left: 620px; }

  /* front */
  .brand {
    position: absolute;
    left: 20px; top: 62px;
    width: 170px;
    text-align: center;
  }
  .brand__mark {
    width: 78px; height: 78px;
    border: 3px solid var(--silver);
    border-radius: 50%;
    margin: 0 auto 16px;
  }
  .brand__name {
    font-size: 14px;
    line-height: 1.2;
    font-weight: 400;
    color: var(--mid-blue);
  }
  .divider-v {
    position: absolute;
    width: 1px;
    background: var(--accent);
  }
  .card--front .divider-v { left: 198px; top: 60px; height: 200px; }
  .contacts {
    position: absolute;
    left: 222px; top: 70px;
    list-style: none;
    font-size: 14.5px;
    line-height: 19px;
  }
  .contacts li { display: flex; align-items: center; gap: 8px; }
  .contacts svg { width: 11px; height: 11px; flex: none; fill: var(--accent); }
  .address {
    position: absolute;
    left: 240px; top: 168px;
    font-size: 15px;
    line-height: 20px;
  }

  /* back */
  .back-brand {
    position: absolute;
    top: 40px; left: 0; right: 0;
    display: flex; align-items: center; justify-content: center; gap: 14px;
  }
  .back-brand__mark {
    width: 62px; height: 62px;
    border: 3px solid var(--silver);
    border-radius: 50%;
  }
  .back-brand__name {
    font-size: 22px;
    font-weight: 600;
    color: var(--silver);
    letter-spacing: .5px;
  }
  .divider-h {
    position: absolute;
    left: 0; right: 0; top: 150px;
    height: 1px;
    background: var(--accent);
  }
  .card--back .divider-v { left: 270px; top: 150px; height: 159px; }
  .partner {
    position: absolute;
    top: 172px;
    width: 270px;
    text-align: center;
  }
  .partner--left { left: 0; }
  .partner--right { left: 270px; }
  .partner__head {
    display: flex; align-items: center; justify-content: center; gap: 8px;
    margin-bottom: 10px;
  }
  .partner__dot { width: 30px; height: 30px; border-radius: 50%; flex: none; }
  .partner--left .partner__dot { background: var(--accent); }
  .partner--right .partner__dot { background: var(--mid-blue); }
  .partner__name { font-size: 13px; font-weight: 700; }
  .partner--left .partner__name { color: var(--accent); }
  .partner--right .partner__name { color: var(--white); letter-spacing: .5px; }
  .partner__city { font-size: 15px; line-height: 20px; }
  .partner__web { font-size: 15px; line-height: 20px; }
  .partner--left .partner__web { color: var(--accent); }
  .partner--right .partner__web { color: var(--mid-blue); }
</style>
</head>
<body>

<section class="card card--front" aria-label="Card front">
  <div class="brand">
    <div class="brand__mark"></div>
    <p class="brand__name">Roshan Barsaz<br>International<br>Transport.Co L.L.c</p>
  </div>
  <div class="divider-v"></div>
  <ul class="contacts">
    <li><svg viewBox="0 0 12 12"><path d="M2.5 0.5l2 2-1 1.5c.6 1.4 1.6 2.4 3 3l1.5-1 2 2-1.5 2C4.5 11.5.5 7.5.5 2z"/></svg>+98 21 66394512</li>
    <li><svg viewBox="0 0 12 12"><path d="M3 0h5l1 1v3h2v8H1V4h2zM4 1v3h4V1zM3 6v1h2V6zm0 2v1h2V8zm4-2v3h2V6z"/></svg>+98 21 66395830</li>
    <li><svg viewBox="0 0 12 12"><path d="M0 2h12v1L6 7 0 3zM0 4.5l6 4 6-4V10H0z"/></svg>info@roshanbarsaz.com</li>
    <li><svg viewBox="0 0 12 12"><circle cx="6" cy="6" r="6"/></svg>www.roshanbarsaz.com</li>
  </ul>
  <p class="address">No.7, 2nd Sarv<br>Baghestan-e-Nouri, Tehran, IR</p>
</section>

<section class="card card--back" aria-label="Card back">
  <div class="back-brand">
    <div class="back-brand__mark"></div>
    <span class="back-brand__name">Roshan Barsaz</span>
  </div>
  <div class="divider-h"></div>
  <div class="divider-v"></div>

  <div class="partner partner--left">
    <div class="partner__head">
      <span class="partner__dot"></span>
      <span class="partner__name">TQM Shipping Line Ltd</span>
    </div>
    <p class="partner__city">London, United Kingdom</p>
    <p class="partner__web">www.tqmline.com</p>
  </div>

  <div class="partner partner--right">
    <div class="partner__head">
      <span class="partner__dot"></span>
      <span class="partner__name">CALM REEF SHIPPING LLC</span>
    </div>
    <p class="partner__city">Dubai, United Arab Emirates</p>
    <p class="partner__web">www.crsuae.com</p>
  </div>
</section>

</body>
</html>
```